Verlin Auto Repair - Flyer Design

My business is a automobile shop where we fix cars. Such things that we do but not limited to is brakes, Engine/Transmission change, Electrical work, emission test, oil change and automobile diagnostic. I am looking for a flyer that will catch peoples attention, I will be giving flyers to people, putting them in car windows and mailboxes. I am looking for a flier that will help to attract more customers to my business. I also want the flyer to say "Bring in your estimate from our competitors with this flyer and we will beat it by 10%" (does not have to be in those exact words). I also want the flyer to have my business address phone and operating hours. I have attached a business card and my business ad which I have placed in the newspaper before. I hope it helps with your design.
Industry/Entity Type
Car Repair
Look and feel
Each slider illustrates characteristics of the customer's brand and the style your logo design should communicate.

```html
<!DOCTYPE html>
<html lang="en">
<head>
<meta charset="utf-8">
<title>Verlin Auto Repair – Flyer</title>
<link rel="stylesheet" href="https://fonts.googleapis.com/css2?family=Fira+Sans:wght@400;500;600&family=Fira+Sans+Condensed:wght@400&family=Lato:wght@400;700&display=swap">
<style>
  :root {
    --canvas: #e9ebee;
    --paper: #ffffff;
    --band-blue: #1f6cc0;
    --navy: #1d3f8a;
    --headline-blue: #2a56a6;
    --accent-red: #c8202f;
    --text-dark: #2a2a2a;
    --ribbon: #f8e6c6;
    --ink: #0b0b0b;
    --offer-green: #6cbf3c;
    --label-yellow: #e6d21c;
    --line: #dadada;
  }
  * { box-sizing: border-box; margin: 0; padding: 0; }
  html, body { width: 943px; height: 1200px; overflow: hidden; }
  body { background: var(--canvas); font-family: "Lato", sans-serif; position: relative; }

  .flyer-slot { position: absolute; left: 41.5px; width: 860px; height: 570px; }
  .flyer-slot--front { top: 20px; }
  .flyer-slot--back { top: 610px; }

  .flyer {
    position: absolute; left: 0; top: 0;
    width: 800px; height: 530px;
    transform: scale(1.075); transform-origin: top left;
    background: var(--paper); overflow: hidden;
    box-shadow: 0 4px 14px rgba(0,0,0,.18);
  }
  .flyer--front { background: linear-gradient(180deg, #ffffff 0%, #ffffff 55%, #eceef1 100%); }

  .brand { position: absolute; }
  .brand__name {
    display: flex; align-items: center; gap: 8px;
    font-family: "Fira Sans", sans-serif; font-weight: 600;
    font-size: 34px; color: var(--navy); letter-spacing: -0.5px; line-height: 1;
  }
  .brand__dot { width: 14px; height: 14px; border-radius: 50%; background: var(--band-blue); }
  .brand__tagline { font-family: "Fira Sans", sans-serif; font-size: 14px; color: #444; margin-top: 6px; margin-left: 4px; }

  /* Front */
  .top-band { position: absolute; left: 0; top: 0; width: 100%; height: 15px; background: linear-gradient(180deg, #2d84d8, var(--band-blue)); }
  .flyer--front .brand { left: 33px; top: 45px; }

  .hours-ribbon {
    position: absolute; left: 612px; top: 15px; width: 146px; height: 258px;
    background: var(--ribbon); text-align: center;
    clip-path: polygon(0 0, 100% 0, 100% 100%, 50% 95%, 0 100%);
    padding-top: 12px;
  }
  .hours-ribbon__title { font-family: "Fira Sans Condensed", sans-serif; color: #666; font-size: 20px; line-height: 1; }
  .hours-ribbon__title strong { display: block; font-weight: 400; font-size: 27px; margin-top: 2px; }
  .hours-ribbon__row { margin: 8px 10px 0; padding-bottom: 8px; border-bottom: 1px solid #e3cfae; font-family: "Fira Sans", sans-serif; font-size: 15px; line-height: 1.25; color: var(--text-dark); }
  .hours-ribbon__row:last-child { border-bottom: none; }
  .hours-ribbon__day { color: var(--accent-red); }
  .hours-ribbon__day--weekday { color: var(--band-blue); }

  .headline { position: absolute; left: 32px; top: 137px; font-family: "Fira Sans", sans-serif; }
  .headline__lead { font-size: 44px; font-weight: 500; color: var(--accent-red); line-height: 1; }
  .headline__main { font-size: 58px; font-weight: 500; color: var(--headline-blue); line-height: 1; margin-top: 4px; letter-spacing: -0.5px; }
  .headline__promise { font-family: "Lato", sans-serif; font-size: 26px; font-weight: 700; color: #777; margin-top: 8px; }

  .car-photo--front {
    position: absolute; left: 272px; top: 305px; width: 522px; height: 160px;
    border-radius: 60px 70px 18px 18px;
    background: linear-gradient(90deg, #3451a8 0%, #2c4690 45%, #1a1a1a 55%, #0d0d0d 100%);
  }

  .office { position: absolute; left: 33px; top: 396px; font-size: 19px; color: #666; line-height: 1.22; font-style: normal; }
  .office__label { font-weight: 700; color: #555; }

  .footer-bar {
    position: absolute; left: 0; bottom: 0; width: 100%; height: 50px; background: var(--ink);
    display: flex; align-items: center; justify-content: center; gap: 38px;
    color: #fff; font-weight: 700; font-size: 20px;
  }

  /* Back */
  .flyer--back .brand { left: 28px; top: 45px; }
  .services { position: absolute; left: 32px; top: 125px; }
  .services__title { font-family: "Fira Sans", sans-serif; font-weight: 600; font-size: 22px; color: var(--navy); }
  .services__cols { display: flex; gap: 18px; margin-top: 10px; }
  .services__list { list-style: none; font-family: "Fira Sans", sans-serif; font-size: 13px; color: var(--text-dark); line-height: 19px; width: 132px; white-space: nowrap; }
  .services__list li::before { content: ""; display: inline-block; width: 4px; height: 4px; border-radius: 50%; background: #999; margin-right: 8px; vertical-align: middle; }

  .coupon {
    position: absolute; top: 37px; width: 132px; height: 140px; text-align: center;
    border: 1px solid var(--line); border-bottom: none; border-radius: 3px 3px 0 0;
    background: linear-gradient(180deg, #f4f4f4 0%, #ffffff 60%);
    font-family: "Fira Sans", sans-serif;
  }
  .coupon--oil { left: 370px; }
  .coupon--repair { left: 508px; }
  .coupon--brakes { left: 646px; }
  .coupon__photo { width: 70px; height: 52px; margin: 12px auto 0; }
  .coupon__photo--oil { background: linear-gradient(135deg, #7a6a48, #3b3b3b); }
  .coupon__photo--tools { background: linear-gradient(135deg, #e2e2e2, #9a9a9a); }
  .coupon__photo--brakes { background: linear-gradient(135deg, #8a8f96, #1f2c3a); }
  .coupon__price { font-size: 22px; color: #555; margin-top: 12px; line-height: 1; }
  .coupon__price small { font-size: 15px; font-weight: 500; }
  .coupon__note { font-size: 12px; color: #777; line-height: 1.1; margin-top: 5px; }
  .coupon__note strong { display: block; font-weight: 400; font-size: 18px; color: #666; margin-top: 6px; }

  .offer-line { position: absolute; left: 370px; width: 410px; top: 198px; text-align: center; font-family: "Fira Sans", sans-serif; font-weight: 500; font-size: 23px; color: var(--offer-green); line-height: 1; }
  .beat-offer { position: absolute; left: 370px; width: 410px; top: 230px; text-align: center; font-family: "Fira Sans", sans-serif; font-size: 13px; color: var(--accent-red); line-height: 1.2; }
  .beat-offer strong { font-weight: 600; }

  .dark-base { position: absolute; left: 0; top: 0; width: 800px; height: 530px; }
  .car-photo--back {
    position: absolute; left: 445px; top: 262px; width: 340px; height: 165px;
    border-radius: 80px 90px 24px 24px;
    background: linear-gradient(160deg, #ffffff 0%, #e6e6e6 55%, #9a9a9a 100%);
  }
  .contact { position: absolute; left: 48px; top: 324px; color: #fff; font-size: 13px; line-height: 19px; }
  .contact__title { font-weight: 700; }
  .contact__label { color: var(--label-yellow); }
  .contact--hours { left: 292px; top: 326px; font-size: 12px; line-height: 15.5px; }
  .contact--hours .contact__title { font-size: 13px; }
  .contact--hours p + p { margin-top: 6px; }
  .contact--hours .contact__title + p { margin-top: 0; }

  .partner-row { position: absolute; left: 0; top: 440px; width: 800px; height: 70px; }
</style>
</head>
<body>

<div class="flyer-slot flyer-slot--front">
  <section class="flyer flyer--front" aria-label="Flyer front">
    <div class="top-band"></div>

    <div class="brand">
      <div class="brand__name">Verlin Auto Repair <span class="brand__dot"></span></div>
      <div class="brand__tagline">Specializing in Foreign &amp; Domestic cars</div>
    </div>

    <aside class="hours-ribbon">
      <div class="hours-ribbon__title">Hours of<strong>Operation</strong></div>
      <div class="hours-ribbon__row"><div class="hours-ribbon__day hours-ribbon__day--weekday">Monday to Friday</div>8am - 5pm</div>
      <div class="hours-ribbon__row"><div class="hours-ribbon__day">SATURDAY</div>8am - 1pm</div>
      <div class="hours-ribbon__row"><div class="hours-ribbon__day">SUNDAY</div>Closed</div>
    </aside>

    <div class="headline">
      <div class="headline__lead">Bring Back That</div>
      <div class="headline__main">NEW CAR FEELING</div>
      <div class="headline__promise">We Get the job Done right the First Time!</div>
    </div>

    <div class="car-photo--front" role="img" aria-label="Photo of a blue convertible and a black SUV side by side"></div>

    <address class="office">
      <div class="office__label">Our Office</div>
      4120 W. Harlan Ave.<br>Brookfield IL. 60513
    </address>

    <footer class="footer-bar">
      <span>Email: VerlinAutoRepair@mailbox.net</span>
      <span>Call Now: (555) 214-7730</span>
    </footer>
  </section>
</div>

<div class="flyer-slot flyer-slot--back">
  <section class="flyer flyer--back" aria-label="Flyer back">
    <svg class="dark-base" viewBox="0 0 800 530" aria-hidden="true">
      <polygon points="0,295 460,295 485,320 800,320 800,530 0,530" fill="#0b0b0b"/>
    </svg>

    <div class="brand">
      <div class="brand__name">Verlin Auto Repair <span class="brand__dot"></span></div>
      <div class="brand__tagline">Specializing in Foreign &amp; Domestic cars</div>
    </div>

    <div class="services">
      <h2 class="services__title">Services</h2>
      <div class="services__cols">
        <ul class="services__list">
          <li>Tune up</li><li>Oil Changes</li><li>Transmissions</li><li>Electrical</li><li>Suspension</li><li>Clutches</li>
        </ul>
        <ul class="services__list">
          <li>A/C Service</li><li>Brakes</li><li>Belts &amp; Hoses</li><li>Exhaust</li><li>Diagnostics</li><li>+So much more</li>
        </ul>
      </div>
    </div>

    <div class="coupon coupon--oil">
      <div class="coupon__photo coupon__photo--oil" role="img" aria-label="Photo of motor oil being poured into an engine"></div>
      <div class="coupon__price">$27.99</div>
      <div class="coupon__note">Oil change with<br>free tire rotaion-fine</div>
    </div>
    <div class="coupon coupon--repair">
      <div class="coupon__photo coupon__photo--tools" role="img" aria-label="Photo of crossed wrenches"></div>
      <div class="coupon__price">$50 <small>OFF</small></div>
      <div class="coupon__note">Any repair over<strong>$400</strong></div>
    </div>
    <div class="coupon coupon--brakes">
      <div class="coupon__photo coupon__photo--brakes" role="img" aria-label="Photo of a brake disc and caliper"></div>
      <div class="coupon__price">$27 <small>OFF</small></div>
      <div class="coupon__note">Oil change with<br>free tire rotaion-fine</div>
    </div>

    <div class="offer-line">Free A/C Performance Check</div>
    <p class="beat-offer">Bring a competitor's estimate with this flyer &ndash; <strong>we'll beat it by 10%</strong></p>

    <div class="car-photo--back" role="img" aria-label="Photo of a white sports SUV"></div>

    <div class="contact">
      <div class="contact__title">Our Office</div>
      4120 W. Harlan Ave.<br>Brookfield IL. 60513<br>
      <span class="contact__label">Email:</span> VerlinAutoRepair@mailbox.net<br>
      <span class="contact__label">Call:</span> (555) 214-7730
    </div>

    <div class="contact contact--hours">
      <p class="contact__title">Hours of Operation</p>
      <p><span class="contact__label">Monday to Friday</span><br>From 8am to 5pm</p>
      <p><span class="contact__label">Saturday:</span> 8am - 1pm</p>
      <p><span class="contact__label">Sunday:</span> Closed</p>
    </div>

    <svg class="partner-row" viewBox="0 0 800 70" aria-label="Row of car makes serviced">
      <g fill="none" stroke="#cfcfcf" stroke-width="3">
        <circle cx="78" cy="32" r="24"/>
        <circle cx="168" cy="32" r="24"/>
        <circle cx="258" cy="32" r="24"/>
        <circle cx="345" cy="32" r="24"/>
        <circle cx="440" cy="32" r="24"/>
        <circle cx="540" cy="32" r="24"/>
        <circle cx="628" cy="32" r="24"/>
        <circle cx="723" cy="32" r="24"/>
      </g>
    </svg>
  </section>
</div>

</body>
</html>
```